Plastic Jar Catalogue 7

We are a plastic factory manufacturing different size of plastic jars, which mostly use for spice and grinded coffee. I need the catalogue to be 3 pages:First page: an attractive cover shows the factory's name and logo with a space for products’ picture. Second page: is an items page which I prefer to be enough for 4 items with a space for item number and description under each item. Last page: to be for factory’s address and contact details.

```html
<!DOCTYPE html>
<html lang="en">
<head>
<meta charset="utf-8">
<title>Clearline Jar Works – Catalogue</title>
<link rel="stylesheet" href="https://fonts.googleapis.com/css2?family=Montserrat:wght@600;700&family=Open+Sans:wght@400;600&display=swap">
<style>
  :root {
    --backdrop: #d3d4d6;
    --paper: #f2f4f5;
    --teal: #1e94b2;
    --green: #8cc63f;
    --ink: #3a3d40;
    --ink-soft: #5b6064;
    --white: #ffffff;
  }
  * { margin: 0; padding: 0; box-sizing: border-box; }
  html, body {
    width: 1200px;
    height: 1200px;
    overflow: hidden;
    background: var(--backdrop);
  }
  .canvas {
    width: 1200px;
    height: 1200px;
    display: flex;
    flex-direction: column;
    align-items: center;
    justify-content: center;
    gap: 60px;
  }
  .spread {
    width: 1000px;
    height: 520px;
    display: block;
    filter: drop-shadow(0 6px 10px rgba(0,0,0,0.12));
  }
  .page { fill: var(--paper); }
  .spine { stroke: #dfe3e5; stroke-width: 2; }
  .band { fill: var(--teal); }
  .corner { fill: var(--green); }
  .brand-name {
    font-family: "Montserrat", sans-serif;
    font-weight: 600;
    fill: var(--teal);
    letter-spacing: 3px;
  }
  .heading {
    font-family: "Open Sans", sans-serif;
    font-weight: 600;
    font-size: 15px;
    fill: var(--ink);
  }
  .body-copy {
    font-family: "Open Sans", sans-serif;
    font-size: 10px;
    fill: var(--ink-soft);
  }
  .banner { fill: var(--teal); }
  .banner-label {
    font-family: "Montserrat", sans-serif;
    font-weight: 700;
    font-size: 22px;
    fill: var(--white);
    letter-spacing: 1px;
  }
  .address-label {
    font-family: "Open Sans", sans-serif;
    font-weight: 600;
    font-size: 10px;
    fill: var(--white);
  }
  .address-copy {
    font-family: "Open Sans", sans-serif;
    font-size: 10px;
    fill: var(--white);
  }
  .hex-frame {
    fill: none;
    stroke: var(--teal);
    stroke-width: 3;
  }
  .jar-photo { fill: url(#jarTone); }
</style>
</head>
<body>
<main class="canvas">

  <!-- Outer covers: back cover (left) and front cover (right) -->
  <svg class="spread spread--cover" viewBox="0 0 1000 520" xmlns="http://www.w3.org/2000/svg">
    <defs>
      <linearGradient id="jarTone" x1="0" y1="0" x2="1" y2="0">
        <stop offset="0" stop-color="#c9d0d4"/>
        <stop offset="0.5" stop-color="#f4f6f7"/>
        <stop offset="1" stop-color="#c3cacf"/>
      </linearGradient>
      <clipPath id="hexA"><polygon points="628,230 604,271.5 556,271.5 532,230 556,188.5 604,188.5"/></clipPath>
      <clipPath id="hexB"><polygon points="700,188.5 676,230 628,230 604,188.5 628,147 676,147"/></clipPath>
      <clipPath id="hexC"><polygon points="628,313 604,354.5 556,354.5 532,313 556,271.5 604,271.5"/></clipPath>
      <clipPath id="hexD"><polygon points="700,271.5 676,313 628,313 604,271.5 628,230 676,230"/></clipPath>
    </defs>

    <rect class="page" x="0" y="0" width="1000" height="520"/>
    <line class="spine" x1="500" y1="0" x2="500" y2="520"/>

    <!-- Back cover -->
    <g class="back-cover">
      <polygon class="band" points="0,30 500,12 500,26 0,44"/>
      <rect class="corner" x="0" y="30" width="14" height="14"/>

      <text class="brand-name" x="250" y="128" font-size="34" text-anchor="middle">CLEARLINE</text>
      <text class="brand-name" x="250" y="160" font-size="18" text-anchor="middle">JAR WORKS</text>

      <text class="heading" x="250" y="218" text-anchor="middle">Lorem ipsum</text>
      <text class="body-copy" text-anchor="middle">
        <tspan x="250" y="236">Clear PET jars made for</tspan>
        <tspan x="250" y="250">spices, herbs and ground</tspan>
        <tspan x="250" y="264">coffee, moulded in sizes</tspan>
        <tspan x="250" y="278">from 100 ml to 1 litre with</tspan>
        <tspan x="250" y="292">screw caps that seal tight</tspan>
        <tspan x="250" y="306">and keep aroma inside.</tspan>
      </text>

      <polygon class="band" points="80,492 180,378 500,318 500,484"/>
      <text class="address-label" x="200" y="404">OUR ADDRES :</text>
      <text class="address-copy">
        <tspan x="200" y="420">12 Harbour Road, Unit 7,</tspan>
        <tspan x="200" y="434">Eastport Industrial Zone</tspan>
        <tspan x="200" y="448">Tel +1 555 0142 386</tspan>
        <tspan x="200" y="462">hello@clearlinejars.com</tspan>
      </text>

      <polygon class="band" points="0,500 500,486 500,500 0,514"/>
      <rect class="corner" x="0" y="500" width="14" height="14"/>
    </g>

    <!-- Front cover -->
    <g class="front-cover">
      <polygon class="band" points="500,12 1000,0 1000,14 500,26"/>

      <text class="brand-name" x="530" y="70" font-size="20">CLEARLINE</text>
      <text class="brand-name" x="530" y="88" font-size="11">JAR WORKS</text>

      <polygon class="banner" points="690,118 1000,98 1000,158 740,160 716,138"/>
      <text class="banner-label" x="790" y="146">CATALOGEU</text>

      <g class="product-hexes">
        <rect class="jar-photo" x="532" y="188.5" width="96" height="83" clip-path="url(#hexA)" role="img" aria-label="Product photo: clear plastic jar with silver lid"/>
        <rect class="jar-photo" x="604" y="147" width="96" height="83" clip-path="url(#hexB)" role="img" aria-label="Product photo: clear plastic jar with silver lid"/>
        <rect class="jar-photo" x="532" y="271.5" width="96" height="83" clip-path="url(#hexC)" role="img" aria-label="Product photo: clear plastic jar with silver lid"/>
        <rect class="jar-photo" x="604" y="230" width="96" height="83" clip-path="url(#hexD)" role="img" aria-label="Product photo: clear plastic jar with silver lid"/>
        <polygon class="hex-frame" points="628,230 604,271.5 556,271.5 532,230 556,188.5 604,188.5"/>
        <polygon class="hex-frame" points="700,188.5 676,230 628,230 604,188.5 628,147 676,147"/>
        <polygon class="hex-frame" points="628,313 604,354.5 556,354.5 532,313 556,271.5 604,271.5"/>
        <polygon class="hex-frame" points="700,271.5 676,313 628,313 604,271.5 628,230 676,230"/>
      </g>

      <path class="band" d="M500,430 Q680,360 840,230 L930,200 Q780,340 560,470 L500,478 Z"/>

      <text class="heading" x="765" y="384">Lorem ipsum</text>
      <text class="body-copy">
        <tspan x="765" y="402">Food-safe jars in every</tspan>
        <tspan x="765" y="416">size your kitchen shelf</tspan>
        <tspan x="765" y="430">needs, made in our own</tspan>
        <tspan x="765" y="444">factory and shipped in</tspan>
        <tspan x="765" y="458">bulk to your door.</tspan>
      </text>

      <polygon class="band" points="500,486 1000,474 1000,488 500,500"/>
      <rect class="corner" x="986" y="460" width="14" height="14"/>
    </g>
  </svg>

  <!-- Inside spread: product items -->
  <svg class="spread spread--inside" viewBox="0 0 1000 520" xmlns="http://www.w3.org/2000/svg">
    <defs>
      <linearGradient id="jarToneInside" x1="0" y1="0" x2="1" y2="0">
        <stop offset="0" stop-color="#c9d0d4"/>
        <stop offset="0.5" stop-color="#f4f6f7"/>
        <stop offset="1" stop-color="#c3cacf"/>
      </linearGradient>
    </defs>

    <rect class="page" x="0" y="0" width="1000" height="520"/>
    <line class="spine" x1="500" y1="0" x2="500" y2="520"/>

    <!-- Left page -->
    <g class="items-left">
      <polygon class="band" points="0,30 500,12 500,26 0,44"/>
      <rect class="corner" x="0" y="30" width="14" height="14"/>

      <text class="heading" x="280" y="90" text-anchor="end">Lorem ipsum</text>
      <text class="body-copy" text-anchor="end">
        <tspan x="280" y="108">Item 01: round PET jar,</tspan>
        <tspan x="280" y="122">250 ml, aluminium lid,</tspan>
        <tspan x="280" y="136">ideal for ground spice</tspan>
        <tspan x="280" y="150">and coffee blends.</tspan>
      </text>
      <rect x="300" y="62" width="110" height="130" rx="10" fill="url(#jarToneInside)" role="img" aria-label="Product photo: item 01, clear plastic jar with silver lid"/>

      <polygon class="banner" points="0,240 395,240 365,290 0,290"/>
      <text class="banner-label" x="30" y="273">OUR PRODUCT</text>

      <rect x="60" y="320" width="120" height="140" rx="10" fill="url(#jarToneInside)" role="img" aria-label="Product photo: item 02, clear plastic jar with silver lid"/>
      <text class="heading" x="210" y="340">Lorem ipsum</text>
      <text class="body-copy">
        <tspan x="210" y="358">Item 02: round PET jar,</tspan>
        <tspan x="210" y="372">500 ml, aluminium lid,</tspan>
        <tspan x="210" y="386">sized for whole beans</tspan>
        <tspan x="210" y="400">and dried herbs.</tspan>
      </text>

      <polygon class="band" points="0,500 500,486 500,500 0,514"/>
    </g>

    <!-- Right page -->
    <g class="items-right">
      <polygon class="band" points="500,12 1000,0 1000,14 500,26"/>

      <rect x="560" y="60" width="130" height="140" rx="10" fill="url(#jarToneInside)" role="img" aria-label="Product photo: item 03, clear plastic jar with silver lid"/>
      <text class="heading" x="720" y="90">Lorem ipsum</text>
      <text class="body-copy">
        <tspan x="720" y="108">Item 03: wide PET jar,</tspan>
        <tspan x="720" y="122">750 ml, aluminium lid,</tspan>
        <tspan x="720" y="136">made for bulk spice</tspan>
        <tspan x="720" y="150">and coffee storage.</tspan>
      </text>

      <polygon class="banner" points="640,240 1000,240 1000,290 640,290 608,265"/>
      <text class="banner-label" x="700" y="273">OUR PRODUCT</text>

      <text class="heading" x="810" y="350" text-anchor="end">Lorem ipsum</text>
      <text class="body-copy" text-anchor="end">
        <tspan x="810" y="368">Item 04: tall PET jar,</tspan>
        <tspan x="810" y="382">1 litre, aluminium lid,</tspan>
        <tspan x="810" y="396">strong for café and</tspan>
        <tspan x="810" y="410">restaurant use daily.</tspan>
      </text>
      <rect x="830" y="330" width="110" height="130" rx="10" fill="url(#jarToneInside)" role="img" aria-label="Product photo: item 04, clear plastic jar with silver lid"/>

      <polygon class="band" points="500,486 1000,474 1000,488 500,500"/>
      <rect class="corner" x="986" y="460" width="14" height="14"/>
    </g>
  </svg>

</main>
</body>
</html>
```